Event Flyer - LGBT Camping Event

I have attached a poster I made (SampleFlyer.pdf) that has all the elements I want. Just don't like the layout and how things look. You can use any colors that make the poster work. I would like to incorporate the Campfire Gathering logo into the flyer (uploaded). You are welcome to grab elements from the event website to incorporate into your design (www.campfiregatheringidaho.org). I included a couple of pictures to possibly use too. Please include all 8 sponsors and the two hosts are the logos on the bottom of sample flyer - Prairie Fairness & Northern Trails Agency. The flyer size needs to be 12"Wide x 17" Tall. Here is a dropbox link to a possible image to use. https://lnk.example/7xQmTza

Please use the wording;

DON’T MISS this LGBT camping event!

Plan the highlight of your summer TODAY.

It’s almost time for the Rocky Mountain Region’s largest LGBT pride camping event: Campfire Gathering Idaho!
Join us August 8th-12th for 5 days of fun in a friendly, safe, LGBT affirming environment for everyone, from everywhere!

More Info or Register Online www.plainsjoy.org

Target Market(s)

LGBT Campers

Industry/Entity Type

Event

Colors

Designer to choose colors to be used in the design.

Requirements
Must have
• Must have text outlined in project description, Campfire Gathering logo, sponsor logos and host logos.

```html
<!DOCTYPE html>
<html lang="en">
<head>
<meta charset="utf-8">
<title>Campfire Gathering Idaho – LGBT Camping Event</title>
<link href="https://fonts.googleapis.com/css2?family=Fredoka:wght@500;600;700&family=Ubuntu:wght@400;500;700&display=swap" rel="stylesheet">
<style>
:root{
  --night:#1f2a4a;
  --pine:#24493f;
  --ember:#e0563b;
  --sun:#f2b544;
  --cream:#fbf6ec;
  --sand:#efe6d4;
  --ink:#1f2a4a;
  --white:#ffffff;
  --muted:#c9d0e0;
}
*{margin:0;padding:0;box-sizing:border-box}
html,body{width:848px;height:1200px;overflow:hidden;background:var(--cream)}
.flyer{width:848px;height:1200px;display:flex;flex-direction:column;background:var(--cream);font-family:"Fredoka",sans-serif;color:var(--ink)}

.masthead{height:200px;flex:none;background:var(--night);padding:30px 40px 0;text-align:center}
.masthead .kicker{display:block;font-weight:700;font-size:78px;line-height:80px;color:var(--ember);letter-spacing:2px;text-transform:uppercase}
.masthead .rest{display:block;font-weight:600;font-size:42px;line-height:52px;color:var(--white)}

.hero{position:relative;height:400px;flex:none;
  background:linear-gradient(160deg,#2f4a6e 0%,#56623f 30%,#b7793a 58%,#d99a4a 72%,#5a3a24 100%)}
.event-mark{position:absolute;right:40px;bottom:-34px;width:230px;height:96px;background:var(--white);
  border:4px solid var(--night);display:flex;align-items:center;justify-content:center;gap:12px;padding:0 14px}
.event-mark .dot{width:14px;height:14px;border-radius:50%;background:var(--ember);flex:none}
.event-mark span{font-weight:600;font-size:22px;line-height:24px;color:var(--night)}

.pitch{height:280px;flex:none;padding:26px 40px 0;text-align:center}
.tagline{font-weight:700;font-size:40px;line-height:44px;color:var(--pine);text-transform:uppercase}
.tagline em{font-style:normal;color:var(--ember)}
.intro{margin-top:14px;font-weight:500;font-size:20px;line-height:28px}
.intro strong{font-weight:700;color:var(--ember)}
.details{margin-top:12px;font-weight:500;font-size:18px;line-height:26px;color:var(--pine)}

.sponsors{height:170px;flex:none;background:var(--sand);padding:14px 40px 0}
.sponsors h3{font-weight:600;font-size:15px;line-height:18px;color:var(--pine);text-transform:uppercase;letter-spacing:2px;text-align:center}
.sponsor-grid{margin-top:10px;display:grid;grid-template-columns:repeat(4,1fr);gap:10px}
.sponsor{height:54px;background:var(--white);border:2px solid var(--pine);display:flex;align-items:center;justify-content:center;
  text-align:center;font-family:"Ubuntu",sans-serif;font-weight:700;font-size:14px;line-height:16px;color:var(--pine);padding:4px}

.footer{flex:1;background:var(--night);color:var(--white);display:flex;align-items:center;gap:26px;padding:0 40px;font-family:"Ubuntu",sans-serif}
.contact{display:flex;flex-direction:column;gap:8px;font-size:14px;line-height:18px;width:230px}
.contact p{display:flex;gap:8px}
.contact svg{flex:none;margin-top:2px}
.register{width:190px;font-size:15px;line-height:20px}
.register b{display:block;font-weight:700;font-size:17px;color:var(--sun)}
.hosts{display:flex;gap:10px}
.host{width:120px;height:84px;background:var(--white);display:flex;align-items:center;justify-content:center;text-align:center;
  font-weight:700;font-size:15px;line-height:18px;color:var(--night);padding:6px}
</style>
</head>
<body>
<main class="flyer">
  <header class="masthead">
    <h1><span class="kicker">Don’t miss</span><span class="rest">this LGBT camping event!</span></h1>
  </header>

  <section class="hero" role="img" aria-label="Photo of campers relaxing beside a tent in an autumn pine forest">
    <div class="event-mark"><i class="dot"></i><span>Campfire Gathering</span></div>
  </section>

  <section class="pitch">
    <h2 class="tagline">Plan the highlight of<br>your summer <em>today.</em></h2>
    <p class="intro">It’s almost time for the Rocky Mountain Region’s largest LGBT pride<br>camping event: <strong>Campfire Gathering Idaho!</strong></p>
    <p class="details">Join us August 8th-12th for 5 days of fun in a friendly, safe,<br>LGBT affirming environment for everyone, from everywhere!</p>
  </section>

  <section class="sponsors">
    <h3>Sponsored By</h3>
    <div class="sponsor-grid">
      <div class="sponsor">Sagebrush Physical Therapy</div>
      <div class="sponsor">Open Ridge Alliance</div>
      <div class="sponsor">meetplains.org</div>
      <div class="sponsor">Y Ranch</div>
      <div class="sponsor">J's Corner Shops</div>
      <div class="sponsor">Walt's Roadside Grill</div>
      <div class="sponsor">Dusty's Boise</div>
      <div class="sponsor">Harlow Finch</div>
    </div>
  </section>

  <footer class="footer">
    <div class="contact">
      <p><svg width="12" height="15" viewBox="0 0 12 15" aria-hidden="true"><path d="M6 0a6 6 0 0 1 6 6c0 4-6 9-6 9S0 10 0 6a6 6 0 0 1 6-6z" fill="var(--sun)"/><circle cx="6" cy="6" r="2.2" fill="var(--night)"/></svg><span>Prairie Fairness<br>PO Box 4417, Pocatello, ID 83201</span></p>
      <p><svg width="14" height="14" viewBox="0 0 14 14" aria-hidden="true"><circle cx="7" cy="7" r="7" fill="var(--sun)"/><path d="M4 5c0-1 1-1.5 1.5-1.5L6.3 5 5.6 6c.4.9 1.2 1.7 2.1 2.1l1-.7L10.3 8.2c0 .5-.5 1.5-1.5 1.5C6 9.7 4 7.5 4 5z" fill="var(--night)"/></svg><span>208 555 0147</span></p>
      <p><svg width="14" height="14" viewBox="0 0 14 14" aria-hidden="true"><circle cx="7" cy="7" r="7" fill="var(--sun)"/><rect x="3.5" y="4.5" width="7" height="5" fill="var(--night)"/><path d="M3.5 4.5 7 7.5l3.5-3" stroke="var(--sun)" stroke-width="1" fill="none"/></svg><span>hello@prairiefairness.org</span></p>
    </div>
    <p class="register">More Info or Register Online<b>www.plainsjoy.org</b></p>
    <div class="hosts">
      <div class="host">Prairie Fairness</div>
      <div class="host">Northern Trails Agency</div>
    </div>
  </footer>
</main>
</body>
</html>
```